Venture firm needs flyer to attract Sales Professionals as Advisors

Creation of either a pdf Flyer or Brochure.
The target audience are senior sales professionals of the Information Technology industry. The flyer needs to come across highly professional, business oriented, positive. Text for the brochure is attached. The colors/graphics should align with Tormid Ventures corporate appearance: www.tormid-example.ventures

Target Market(s)

Sales Professionals in the Information Technology Industry

Industry/Entity Type

Information Technology

Font styles to use
Other font styles liked:
• Raleway

Requirements
Must have
• fitting the corporate look and feel: www.tormid-example.ventures

```html
<!DOCTYPE html>
<html lang="en">
<head>
<meta charset="utf-8">
<title>Tormid Ventures – Sales Council Flyer</title>
<link rel="stylesheet" href="https://fonts.googleapis.com/css2?family=Raleway:wght@300;400&family=Roboto:wght@300;400;700&family=Roboto+Condensed:wght@400;700&family=Oswald:wght@600&display=swap">
<style>
  :root{
    --navy:#0f3461;
    --tile:#2e4772;
    --band:#5b8fbf;
    --ink:#1f1f1f;
    --accent:#2b2d8e;
    --paper:#ffffff;
    --stage:#2a4868;
  }
  *{box-sizing:border-box;margin:0;padding:0}
  html,body{width:1200px;height:1200px;overflow:hidden;background:var(--stage)}
  .flyer{
    position:absolute;left:151px;top:20px;width:984px;height:1272px;
    transform:scale(0.912);transform-origin:top left;
    background:var(--paper);font-family:"Roboto Condensed",Arial,sans-serif;color:var(--ink);
  }
  .masthead{height:112px;background:var(--navy);display:flex;align-items:flex-end;justify-content:center;padding-bottom:10px}
  .masthead .brand{font-family:"Raleway",sans-serif;font-weight:300;font-size:56px;letter-spacing:1px;color:#fff}
  .body{position:absolute;top:112px;left:0;width:984px;height:1022px}
  .visuals{position:absolute;left:51px;top:0;width:441px;height:1022px}
  .photo{position:absolute}
  .hero{left:0;top:0;width:441px;height:284px;background:linear-gradient(170deg,#6f8fb0 0%,#c9d6e2 45%,#eef2f6 80%,#aebfd0 100%)}
  .tagline{position:absolute;left:0;top:284px;width:441px;height:109px;background:var(--band);color:#fff;text-align:center;padding-top:6px}
  .tagline .lead{font-family:"Roboto",sans-serif;font-weight:300;font-size:25px;line-height:31px}
  .tagline .big{font-family:"Oswald",sans-serif;font-weight:600;font-size:36px;line-height:40px;letter-spacing:.5px}
  .tile{position:absolute;width:221px;height:153px}
  .tile.text{background:var(--tile);color:#fff;display:flex;align-items:center;justify-content:center;text-align:center;font-family:Arial,Helvetica,sans-serif;font-weight:700;font-size:17.5px;line-height:20.5px;padding:0 10px}
  .snow{background:linear-gradient(180deg,#9fb3c9,#eef2f6 60%,#dfe6ee)}
  .sky{background:linear-gradient(180deg,#dfe8f2,#b9c8d8 55%,#6d5a48)}
  .red{background:linear-gradient(135deg,#b5435f,#e3a0b0 50%,#8e2f49)}
  .slope{background:linear-gradient(200deg,#e9eef3,#c2ccd6 60%,#f4f6f8)}
  .copy{position:absolute;left:506px;top:0;width:431px}
  .copy h1{font-family:"Roboto",sans-serif;font-weight:400;color:var(--accent);font-size:45px;line-height:52px;margin-top:0}
  .copy p{font-size:16.6px;line-height:21px;text-align:justify;margin-top:5px}
  .copy h2{font-family:"Roboto Condensed",sans-serif;font-weight:700;color:var(--accent);font-size:29px;line-height:34px;margin-top:8px}
  .copy p.strong{font-weight:700;font-size:20px;line-height:25px}
  .copy .first{margin-top:8px}
  .footer{position:absolute;left:0;top:1134px;width:984px;height:138px;background:var(--navy);color:#fff;display:flex;align-items:center;justify-content:center;font-family:"Raleway",sans-serif;font-size:14.5px;line-height:17px;text-align:center}
  .footer .office{width:340px}
  .footer .office b{font-family:Arial,sans-serif;font-weight:700}
  .footer .mid{width:225px;border-left:1px solid #fff;border-right:1px solid #fff;padding:10px 0}
  .footer .mid .name{font-weight:300;font-size:20px;letter-spacing:.3px}
  .footer .mid .web{font-size:9px;letter-spacing:3px;margin-top:6px}
</style>
</head>
<body>
<main class="flyer">
  <header class="masthead"><span class="brand">TORMID VENTURES</span></header>

  <section class="body">
    <div class="visuals">
      <div class="photo hero" role="img" aria-label="Mountaineer in bright jacket standing on a snowy summit"></div>
      <div class="tagline">
        <div class="lead">Investing in Global<br>Go-to-Market Strategies</div>
        <div class="big">ACHIEVING GROWTH</div>
      </div>
      <div class="tile snow" style="left:0;top:393px" role="img" aria-label="Hiker walking across a snowfield"></div>
      <div class="tile text" style="left:220px;top:393px">Expand<br>Internationally</div>
      <div class="tile text" style="left:0;top:550px">Leverage<br>Channel and<br>Technology<br>Partners</div>
      <div class="tile sky" style="left:220px;top:550px" role="img" aria-label="Climber reaching down to help another up a rock"></div>
      <div class="tile red" style="left:0;top:707px" role="img" aria-label="Racers in red suits in motion"></div>
      <div class="tile text" style="left:220px;top:707px">Build a high<br>performance<br>Sales engine<br>predictable &amp; scalable</div>
      <div class="tile text" style="left:0;top:865px">Improve Productivity<br>with<br>Velocity Sales</div>
      <div class="tile slope" style="left:220px;top:865px" role="img" aria-label="Skier carving through powder snow"></div>
    </div>

    <article class="copy">
      <h1>Tormid Sales<br>Council (TSC)</h1>
      <p class="first">The TSC is a by invitation only global community of high caliber Sales Professionals in the IT industry. Participating in the TSC provides significant wealth creation opportunities by earning consulting fees and sales commission or finding an exciting startup to work for.</p>
      <p>TSC members actively collaborate with each other to close deals, generate leads &amp; opportunities, navigate through client organizations and build a true advisory status with customers.</p>
      <p>TSC members get early first hand visibility into the latest technology innovations and learn how those technologies could assist their clients in solving their complex business objectives.</p>
      <h2>How it works :</h2>
      <p>TSC members will be introduced to Tormid Ventures’ client and portfolio companies. This unique ability to learn about latest technology innovation keeps the participants up to date with industry trends and could open interesting earning or employment opportunities.</p>
      <p>Once exposed to a specific vendor, TSC members can decide if and how they would like to get further involved. Dependent on the interest level for the specific technology, the ability to offer a solution to a known customer problem or the sheer interest to develop new business, TSC members can participate in two ways:</p>
      <h2>As Associates :</h2>
      <p>Associates are actively selling and promoting one or more Tormid Ventures´ portfolio companies. This could be an employment or a freelance opportunity.</p>
      <h2>As Advisors :</h2>
      <p class="strong">Advisors offer their contacts and knowledge about customers to Associates.</p>
      <p>Advisors could create leads, support with introductions, explain customer organization and processes etc. They will be compensated by Associates with a pre-negotiated % of commission of a future sale that was supported by the Advisor.</p>
      <p>Whatever level of involvement a TSC member seeks there is plenty of opportunity to be rewarded for working with fellow Sales Professionals and Great Startups on the forefront of technical innovation.</p>
    </article>
  </section>

  <footer class="footer">
    <div class="office"><b>USA</b><br>240 Harbor Lane<br>Palo Verde, CA 94099<br>Tel : +1-555-010 2040 | info@tormid-example.ventures</div>
    <div class="mid"><div class="name">TORMID VENTURES</div><div class="web">www.tormid-example.ventures</div></div>
    <div class="office"><b>EUROPE</b><br>Lindenweg 7<br>10999 Berlin - Germany<br>Tel : +49 170 0000123 | info@tormid-example.ventures</div>
  </footer>
</main>
</body>
</html>
```